Buch-/E-Book-Cover
Zielgruppe
Wir verkaufen Trainings und vermitteln über unser Buch ein erstes vertieftes Wissen zum Thema Vermögensaufbau.
Aufgabenstellung
Es soll schlicht und schön sein, Angelehnt an Tall coin short coin, bzw. an Schau hin und bleib Klug von Bartholo Fenwick.
Wir benötigen die AI, etc Dateien und die fertigen Dateien für Velmora.de Lumora sowie Velmora.de Books (ehemals Printvale) mit fertigem Cover.
Vorgaben von Velmora.de über die Homepage. Anbei ein Beispiel (wegen Velmora.de Buchnummer etc) Abstände, Buchrücken etc.
Buch ca. 150 Seiten
https://www.velmora-beispiel.de/Gaertner-bleiben-heute-Zeichen-guten/dp/7392058164 Front und Backcover kann man sich da ansehen.
Der Buchtitel ist 'Baue Kredite und bleib frei' - - Lassen Sie uns freundschaftlich in entspannter Atmosphäre über Immobilien sprechen (der nebentitel so klein wie bei Tall Coin - Short Coin)
Rücktitel: Bitte zuerst Platzhalter.
Ich bitte um 5x8 inch, also wie DIN A 5, wir nehmen cremefarbenes Papier denke ich. Die Seitenzahl kann ich auf die Seite noch nicht sagen, wir haben aber 75 Din A4 Seiten, sprich nach Formatierung eher 160-165 Din A5. WErde ich Ihnen final nach dem Gewinn sagen.
Versuchen Sie mich mal aus dem einen Bild raus zu schneiden, und dass dann mit einem Layer über das cover zu legen.
2-3 Versionen wäre gut, mit 2-3 Bildern. Buchrücken ein kleines Bild von mir.
Seite vom Buch: Titel nochmal.

```html
<!DOCTYPE html>
<html lang="de">
<head>
<meta charset="utf-8">
<title>Baue Kredite und bleib frei – Buchcover</title>
<link rel="stylesheet" href="https://fonts.googleapis.com/css2?family=Open+Sans:wdth,wght@75..100,600..800&display=swap">
<style>
  :root {
    --purple-deep: #1f0324;
    --purple-dark: #3a0a40;
    --purple-mid: #7a3a85;
    --title-yellow: #f9d423;
    --text-white: #ffffff;
    --text-silver: #e9e6ec;
    --placeholder-white: #ffffff;
  }
  * { margin: 0; padding: 0; box-sizing: border-box; }
  html, body { width: 1200px; height: 927px; overflow: hidden; background: var(--purple-deep); }
  .cover-spread {
    position: relative;
    width: 1200px;
    height: 927px;
    overflow: hidden;
    background:
      radial-gradient(ellipse 480px 420px at 900px 90px, rgba(200,150,210,0.75), transparent 70%),
      radial-gradient(ellipse 520px 600px at 880px 380px, rgba(140,70,150,0.6), transparent 75%),
      radial-gradient(ellipse 520px 520px at 300px 300px, rgba(110,40,120,0.45), transparent 75%),
      linear-gradient(180deg, var(--purple-dark) 0%, #4a1352 45%, var(--purple-deep) 100%);
    font-family: "Open Sans", sans-serif;
  }
  /* Back cover */
  .back-heading {
    position: absolute;
    left: 44px; width: 504px; top: 46px;
    text-align: center;
    font-weight: 700;
    font-stretch: 75%;
    font-size: 24px;
    color: var(--title-yellow);
  }
  .back-blurb {
    position: absolute;
    left: 44px; width: 504px; top: 95px;
    color: var(--text-white);
    font-weight: 700;
    font-stretch: 75%;
    font-size: 18px;
    line-height: 21.9px;
    text-align: justify;
  }
  .back-blurb p + p { margin-top: 21.9px; }
  .speaker-photo {
    position: absolute;
    left: 47px; top: 560px; width: 250px; height: 358px;
    background: radial-gradient(ellipse 60% 55% at 50% 55%, #6a5a5e, #3a2a36 60%, transparent 100%);
    border-radius: 40px 40px 0 0;
    opacity: 0.9;
  }
  .isbn-placeholder {
    position: absolute;
    left: 325px; top: 754px; width: 223px; height: 131px;
    background: var(--placeholder-white);
  }
  /* Spine */
  .spine { position: absolute; left: 574px; top: 0; width: 47px; height: 927px; }
  /* Front cover */
  .front-author { position: absolute; left: 650px; top: 34px; width: 508px; height: 30px; }
  .portrait-photo {
    position: absolute;
    left: 610px; top: 253px; width: 435px; height: 643px;
    background:
      radial-gradient(ellipse 40% 30% at 48% 30%, #c99a85, #8a5f50 60%, transparent 100%),
      radial-gradient(ellipse 30% 20% at 52% 62%, #b9d4ec, transparent 100%),
      linear-gradient(180deg, transparent 0%, rgba(60,45,45,0.6) 45%, #3b3230 70%, #2a2322 100%);
    border-radius: 180px 180px 0 0;
  }
  .title-art { position: absolute; left: 621px; top: 0; width: 579px; height: 927px; }
  .subtitle-label {
    position: absolute;
    right: 46px; top: 358px;
    text-align: right;
    color: var(--text-silver);
    text-shadow: 1px 1px 2px rgba(0,0,0,0.6);
  }
  .subtitle-label .small { font-weight: 600; font-size: 19px; letter-spacing: 1.5px; }
  .subtitle-label .large { font-weight: 800; font-size: 28px; letter-spacing: 0.5px; margin-top: 12px; }
  .tagline {
    position: absolute;
    left: 880px; width: 310px; top: 554px;
    text-align: center;
    color: var(--text-white);
    font-weight: 600;
    font-size: 17px;
    line-height: 23.5px;
    text-shadow: 1px 1px 2px rgba(0,0,0,0.7);
  }
</style>
</head>
<body>
<main class="cover-spread">

  <!-- Back cover -->
  <h2 class="back-heading">BAUE KREDITE UND BLEIB FREI!</h2>
  <div class="back-blurb">
    <p>Das klingt für Sie nach Widerspruch? Dann kennen Sie WohnwertCoach Tarek Morvan (Ex-Lehrer) noch nicht: Schritt für Schritt berichtet er von seinem erstaunlichen Werdegang und seinem Erfolg als Immobilieninvestor. Erfahren Sie von ihm aus erster Hand, wie Sie an Ihr Start-Objekt gelangen und auf dem Immobilienmarkt bestehen. Als ehemalige Lehrkraft bringt Tarek Morvan die Dinge allgemein verständlich und gebündelt auf den Punkt. Profitieren Sie von seiner breiten Erfahrung, lernen Sie aus den im Ratgeber aufgeführten, persönlichen Gesprächen, alles, was Sie wissen müssen – und werden Sie selbst zum WohnwertCoach.</p>
    <p>Ein Denkanstoß gefällig? Bei derzeit 1 % Zinsen und gleichzeitiger Inflation von 3 % können Sie praktisch dabei zusehen, wie Ihre Schulden mit jedem Tag schrumpfen.</p>
    <p>Praxisrelevant, authentisch und auf Augenhöhe mit seinen Lesern – der WohnwertCoach bietet Ihnen in „Baue Kredite und bleib frei!“ alles, um noch heute mit einem neuen, unabhängigen Leben zu beginnen. Fangen Sie gleich damit an!</p>
  </div>
  <div class="speaker-photo" role="img" aria-label="Foto des Autors auf der Bühne, einen Geldschein in die Höhe haltend"></div>
  <div class="isbn-placeholder"></div>

  <!-- Spine -->
  <svg class="spine" viewBox="0 0 47 927" aria-label="Buchrücken">
    <text transform="translate(15 44) rotate(90)" textLength="236" lengthAdjust="spacingAndGlyphs"
          font-family="Open Sans, sans-serif" font-weight="800" font-size="25" fill="#ffffff">TAREK MORVAN</text>
    <text transform="translate(15 434) rotate(90)" textLength="451" lengthAdjust="spacingAndGlyphs"
          font-family="Open Sans, sans-serif" font-weight="800" font-size="25" fill="#f9d423">BAUE KREDITE UND BLEIB FREI</text>
  </svg>

  <!-- Front cover -->
  <div class="portrait-photo" role="img" aria-label="Porträtfoto des Autors in Sakko und hellblauem Hemd"></div>
  <svg class="front-author" viewBox="0 0 508 30" aria-label="Tarek Morvan - der WohnwertCoach">
    <text x="0" y="24" textLength="507" lengthAdjust="spacingAndGlyphs"
          font-family="Open Sans, sans-serif" font-weight="800" font-size="21" fill="#ffffff">TAREK MORVAN - DER WOHNWERTCOACH</text>
  </svg>

  <svg class="title-art" viewBox="0 0 579 927" aria-label="Baue Kredite und bleib frei">
    <defs>
      <filter id="title-shadow" x="-5%" y="-10%" width="110%" height="130%">
        <feDropShadow dx="2" dy="3" stdDeviation="2" flood-color="#000" flood-opacity="0.45"/>
      </filter>
    </defs>
    <g font-family="Open Sans, sans-serif" font-weight="800" fill="#f9d423" filter="url(#title-shadow)">
      <text x="29" y="187" font-size="146" textLength="502" lengthAdjust="spacingAndGlyphs">BAUE</text>
      <text x="29" y="280" font-size="92" textLength="506" lengthAdjust="spacingAndGlyphs">KREDITE</text>
      <text x="29" y="750" font-size="44" textLength="89" lengthAdjust="spacingAndGlyphs">und</text>
      <text x="151" y="750" font-size="76" textLength="294" lengthAdjust="spacingAndGlyphs">BLEIB</text>
      <text x="29" y="885" font-size="172" textLength="504" lengthAdjust="spacingAndGlyphs">FREI</text>
    </g>
  </svg>

  <div class="subtitle-label">
    <div class="small">GESPRÄCHE ÜBER</div>
    <div class="large">IMMOBILIEN</div>
  </div>
  <p class="tagline">Lassen Sie uns freundschaftlich<br>in entspannter Atmosphäre<br>über Immobilien sprechen</p>

</main>
</body>
</html>
```